Wildlife photographer Website

The website is to be a "resume" of pictures and awards won by Nora. Lean heavy to outdoor wildlife.
She will post articles and have ability to interact with fans.

I will add some of her pictures tonight,

Target Market(s)

Terra Quarterly .....anyone looking to hire a wildlife photographer.

Industry/Entity Type

Professional Photography

Contact Information for Business Card

Nora Falkett
4817 Maple Hollow Lane
Columbia MD 21078
443-581-2094
Nora@FernOwlPix.com

Coding

Coded - Design and coding required

Number of Pages Required

5+ page

Requirements
Must have
• New Logo
Nice to have
• Nature, and eye catching graphics

```html
<!DOCTYPE html>
<html lang="en">
<head>
<meta charset="utf-8">
<title>Nora Falkett — Wildlife Photographer</title>
<link rel="stylesheet" href="https://fonts.googleapis.com/css2?family=Anton&family=Lato:wght@400;700&display=swap">
<style>
:root{
  --red:#e0101f;
  --ink:#1a1a1a;
  --white:#ffffff;
  --muted:#444444;
  --award-bg:#f1eeee;
  --footer:#050505;
  --gold:#d9a21c;
  --display:"Anton",Impact,sans-serif;
  --body:"Lato",Arial,sans-serif;
}
*{box-sizing:border-box;margin:0;padding:0}
html,body{width:1200px;height:3299px;overflow:hidden;background:var(--white)}
body{position:relative;font-family:var(--body);color:var(--ink)}
.abs{position:absolute}

/* Hero */
.hero{position:absolute;left:0;top:0;width:1200px;height:593px;
  background:radial-gradient(ellipse at 60% 35%,#6d7570 0%,#3a4441 35%,#1d2422 70%,#121614 100%)}
.brand{left:111px;top:26px;font-family:var(--display);font-size:34px;color:var(--white);letter-spacing:.5px;line-height:1}
.nav{top:38px;display:flex;gap:0;font-family:var(--display);font-size:14px;color:var(--white);letter-spacing:.3px}
.nav a{position:absolute;color:var(--white);text-decoration:none;white-space:nowrap}
.nav a.active{color:var(--red)}
.call-icon{left:890px;top:22px;width:46px;height:46px;border-radius:50%;background:var(--red)}
.call-label{left:950px;top:25px;font-size:12px;color:var(--red)}
.call-number{left:950px;top:43px;font-family:var(--display);font-size:21px;color:var(--white);letter-spacing:.3px}
.hero-title{font-family:var(--display);font-size:178px;line-height:1;color:#f6eef0;letter-spacing:2px}
.hero-sub{left:0;width:1200px;top:390px;text-align:center;font-family:var(--display);font-size:58px;color:var(--red);letter-spacing:.5px}

/* About */
.portrait{left:83px;top:675px;width:496px;height:414px;border-radius:46% 40% 44% 38%;
  background:linear-gradient(135deg,#5b564e 0%,#2c2c2e 55%,#1c2025 100%)}
.eyebrow{left:599px;top:696px;font-family:var(--display);font-size:16px;color:var(--red)}
.section-heading{font-family:var(--display);font-size:38px;line-height:1.1;color:var(--ink);letter-spacing:.2px}
.section-heading em{font-style:normal;color:var(--red)}
.rule{height:2px;width:63px;background:var(--red)}
.about-text{left:599px;top:800px;width:490px;font-size:15.5px;line-height:30px;color:var(--muted)}
.btn{display:flex;align-items:center;justify-content:center;font-family:var(--display);font-size:16px;border:2px solid var(--ink);color:var(--ink)}

/* Gallery */
.gallery{position:absolute;left:0;top:1183px;width:1200px;height:628px;overflow:hidden;
  background:linear-gradient(180deg,#2a2118 0%,#3b2d1c 22%,#1f1a15 45%,#151311 100%)}
.gallery .section-heading{color:var(--white)}
.gallery-text{left:112px;top:168px;width:700px;font-size:15px;line-height:30px;color:#e6e6e6}
.thumb{top:269px;width:190px;height:264px}

/* Articles */
.card{background:var(--white);box-shadow:0 0 10px rgba(0,0,0,.12)}
.card-img{position:absolute;left:6px;top:6px;right:6px}
.card-title{position:absolute;left:0;right:0;text-align:center;font-family:var(--display);font-size:16px;color:var(--ink)}
.card-text{position:absolute;left:20px;right:20px;text-align:center;font-size:13.5px;line-height:31px;color:var(--muted)}
.card-meta{position:absolute;left:0;right:0;display:flex;justify-content:center;gap:52px;font-size:13.5px;color:var(--muted)}
.card-meta span{display:flex;align-items:center;gap:6px}

/* Awards */
.awards{position:absolute;left:0;top:2824px;width:1200px;height:374px;background:var(--award-bg)}
.award{top:177px;width:188px;height:95px;background:var(--white);box-shadow:0 0 8px rgba(0,0,0,.06)}
.award-art{position:absolute;left:70px;top:16px;width:48px;height:62px;border-radius:6px;
  background:linear-gradient(160deg,#f4cd4f,var(--gold) 60%,#9c6b0c)}

.footer{position:absolute;left:0;top:3198px;width:1200px;height:101px;background:var(--footer);
  display:flex;align-items:center;justify-content:center;font-size:12px;color:var(--white);letter-spacing:.2px}
.center{left:0;width:1200px;text-align:center}
</style>
</head>
<body>

<header class="hero" role="img" aria-label="Elephant walking through a misty forest at dawn">
  <div class="abs brand">NORA FALKETT</div>
  <nav class="abs nav" style="left:0;top:38px">
    <a class="active" style="left:487px">HOME</a>
    <a style="left:547px">ABOUT ME</a>
    <a style="left:633px">ARTICLE</a>
    <a style="left:697px">GALLERY</a>
    <a style="left:771px">CONTACT US</a>
  </nav>
  <div class="abs call-icon">
    <svg width="46" height="46" viewBox="0 0 46 46"><path d="M18 16c1 3 4 8 9 11l2-2c.5-.5 1.2-.5 1.7-.2l2.3 1.5c.6.4.7 1.2.2 1.7l-1.6 1.8c-1 1-2.6 1.2-3.9.5-5-2.7-9-7-11-12-.5-1.3-.2-2.8.8-3.7l1.7-1.5c.5-.4 1.3-.3 1.7.2l1.3 2.3c.3.6.2 1.2-.3 1.7z" fill="#fff"/></svg>
  </div>
  <div class="abs call-label">Call Us Today</div>
  <div class="abs call-number">+123 456 7890</div>
  <div class="abs hero-title" style="left:218px;top:180px">WILD</div>
  <div class="abs hero-title" style="left:738px;top:180px">LIFE</div>
  <div class="abs hero-sub">PHOTOGRAPHER</div>
</header>

<section aria-label="About me">
  <div class="abs portrait" role="img" aria-label="Portrait of Nora holding a camera with a long lens over a brushstroke backdrop"></div>
  <div class="abs eyebrow">ABOUT ME</div>
  <h2 class="abs section-heading" style="left:599px;top:724px">HI ! I AM <em>WILDLIFE PHOTOGRAPHER</em></h2>
  <div class="abs rule" style="left:600px;top:780px"></div>
  <p class="abs about-text">Lorem ipsum dolor sit amet, consectetur adipiscing elit, sed do eius­mod tempor incididunt ut labore et dolore magna aliqua. Quis ipsum suspendisse ultrices gravida. Risus commodo viverra maecenas ac­cumsan lacus vel facilisis. Lorem ipsum dolor sit amet, consectetur adipiscing elit, sed do eiusmod tempor incididunt ut labore et dolore magna aliqua. Quis ipsum suspendisse ultrices.</p>
  <div class="abs btn" style="left:598px;top:1010px;width:160px;height:49px">ABOUT ME</div>
</section>

<section class="gallery" role="region" aria-label="Photo gallery">
  <h2 class="abs section-heading" style="left:111px;top:87px"><em>OUR</em> PHOTO GALLERY</h2>
  <div class="abs rule" style="left:112px;top:146px;width:82px"></div>
  <div class="abs btn" style="left:926px;top:86px;width:160px;height:48px;border-color:#fff;color:#fff">VIEW MORE</div>
  <p class="abs gallery-text">Lorem ipsum dolor sit amet, consectetur adipiscing elit, sed do eiusmod tempor incididunt ut labore et dolore magna aliqua. Quis ipsum suspendisse ultrices gravida. Risus commodo.</p>
  <div class="abs thumb" style="left:213px;background:linear-gradient(180deg,#b8a28a,#c9703a 55%,#e7e3de)" role="img" aria-label="Red fox standing in snow"></div>
  <div class="abs thumb" style="left:432px;background:linear-gradient(180deg,#3b3526,#6e5a3f 50%,#1d1d1d)" role="img" aria-label="Hooded mergansers on water"></div>
  <div class="abs thumb" style="left:651px;background:linear-gradient(180deg,#c4c8c4,#e9ebe6 50%,#9aa2a0)" role="img" aria-label="Swan spreading its wings"></div>
  <div class="abs thumb" style="left:870px;background:linear-gradient(180deg,#1f3d6b,#2c5388 50%,#15305a)" role="img" aria-label="Loon swimming on blue water"></div>
  <div class="abs thumb" style="left:1089px;background:linear-gradient(180deg,#9a7438,#c3964d 50%,#5b4224)" role="img" aria-label="Otter by the water"></div>
</section>

<section aria-label="Latest articles">
  <h2 class="abs section-heading center" style="top:1898px">OUR <em>LATEST ARTICLES</em></h2>
  <div class="abs rule" style="left:559px;top:1955px;width:82px"></div>

  <article class="abs card" style="left:111px;top:1999px;width:479px;height:422px">
    <div class="card-img" style="height:275px;background:linear-gradient(180deg,#b23a2f,#d9603f 35%,#3b2628 60%,#5a3a35)" role="img" aria-label="Red sun setting over a calm bay"></div>
    <div class="card-title" style="top:294px">CONSECTETUR ADIPISCING ELIT</div>
    <p class="card-text" style="top:314px">Lorem ipsum dolor sit amet, consectetur adipiscing elit, sed do eius­mod tempor incididunt ut labore et dolore magna aliqua.</p>
    <div class="card-meta" style="top:383px"><span>💬︎ 1.5K Comment</span><span>👍︎ 1.5K Like</span></div>
  </article>
  <article class="abs card" style="left:607px;top:1999px;width:482px;height:422px">
    <div class="card-img" style="height:275px;background:linear-gradient(180deg,#2d5a93,#1f4a80 60%,#2a5690)" role="img" aria-label="Gull diving over blue water"></div>
    <div class="card-title" style="top:294px">CONSECTETUR ADIPISCING ELIT</div>
    <p class="card-text" style="top:314px">Lorem ipsum dolor sit amet, consectetur adipiscing elit, sed do eius­mod tempor incididunt ut labore et dolore magna aliqua.</p>
    <div class="card-meta" style="top:383px"><span>💬︎ 1.5K Comment</span><span>👍︎ 1.5K Like</span></div>
  </article>

  <article class="abs card" style="left:111px;top:2444px;width:318px;height:271px">
    <div class="card-img" style="height:181px;background:linear-gradient(180deg,#6b5446,#8e735f 60%,#5a4a40)" role="img" aria-label="Towhee perched on a branch"></div>
    <div class="card-title" style="top:200px">CONSECTETUR ADIPISCING ELIT</div>
    <div class="card-meta" style="top:238px"><span>💬︎ 1.5K Comment</span><span>👍︎ 1.5K Like</span></div>
  </article>
  <article class="abs card" style="left:439px;top:2444px;width:319px;height:271px">
    <div class="card-img" style="height:181px;background:linear-gradient(180deg,#1d3552,#27466a 60%,#162a42)" role="img" aria-label="Harlequin duck swimming"></div>
    <div class="card-title" style="top:200px">CONSECTETUR ADIPISCING ELIT</div>
    <div class="card-meta" style="top:238px"><span>💬︎ 1.5K Comment</span><span>👍︎ 1.5K Like</span></div>
  </article>
  <article class="abs card" style="left:768px;top:2444px;width:321px;height:271px">
    <div class="card-img" style="height:181px;background:linear-gradient(180deg,#8e8578,#a39a8c 60%,#6f685e)" role="img" aria-label="Hummingbird drinking from a trickle of water"></div>
    <div class="card-title" style="top:200px">CONSECTETUR ADIPISCING ELIT</div>
    <div class="card-meta" style="top:238px"><span>💬︎ 1.5K Comment</span><span>👍︎ 1.5K Like</span></div>
  </article>
</section>

<section class="awards" aria-label="Awards">
  <h2 class="abs section-heading center" style="top:77px">WILDNORA <em>AWARD</em></h2>
  <div class="abs rule" style="left:548px;top:134px;width:82px"></div>
  <div class="abs award" style="left:111px"><div class="award-art" role="img" aria-label="Gold trophy cup"></div></div>
  <div class="abs award" style="left:309px"><div class="award-art" role="img" aria-label="Gold figure statuette"></div></div>
  <div class="abs award" style="left:506px"><div class="award-art" role="img" aria-label="Gold star award"></div></div>
  <div class="abs award" style="left:703px"><div class="award-art" role="img" aria-label="Gold camera on a stand"></div></div>
  <div class="abs award" style="left:900px"><div class="award-art" role="img" aria-label="Gold camera trophy"></div></div>
</section>

<footer class="footer">© COPYRIGHTS 2021 COMPANY NAME &nbsp; | &nbsp; ALL RIGHTS RESERVED</footer>

</body>
</html>
```